Professional individual needs business card design

I need a business card designed for my friend to show their skills and contact details

I would like to see pattern designs with a black foreground and strong look - will submit content specifics but basics are:

NAME SURNAME (large and bold)
Event Manager & MC

Tressel Magazine
The other event I run

phone number - email

```html
<!DOCTYPE html>
<html lang="en">
<head>
<meta charset="utf-8">
<title>Reid Calder – Business Card</title>
<link rel="stylesheet" href="https://fonts.googleapis.com/css2?family=Limelight&family=Questrial&display=swap">
<style>
  :root {
    --backdrop: #ebe8e3;
    --card-ink: #17171b;
    --card-ink-soft: #212127;
    --text-light: #f4f4f4;
    --text-muted: #d9d9dc;
  }

  html, body {
    margin: 0;
    padding: 0;
    width: 1200px;
    height: 900px;
    overflow: hidden;
    background: var(--backdrop);
  }

  .canvas {
    position: relative;
    width: 1200px;
    height: 900px;
  }

  .business-card {
    position: absolute;
    left: 160px;
    top: 190px;
    width: 880px;
    height: 520px;
    background: var(--card-ink);
    box-shadow: 0 18px 40px rgba(0, 0, 0, 0.18);
    overflow: hidden;
    font-family: "Questrial", sans-serif;
    color: var(--text-light);
  }

  .card-texture {
    position: absolute;
    inset: 0;
    background: linear-gradient(135deg, var(--card-ink-soft) 0%, var(--card-ink) 55%, var(--card-ink-soft) 100%);
  }

  .card-content {
    position: absolute;
    inset: 0;
    display: flex;
    flex-direction: column;
    align-items: center;
    padding-top: 92px;
  }

  .holder-name {
    margin: 0;
    font-family: "Limelight", serif;
    font-weight: 400;
    font-size: 58px;
    letter-spacing: 0.5px;
    line-height: 1;
  }

  .holder-role {
    margin: 20px 0 0;
    font-size: 24px;
    letter-spacing: 0.5px;
    color: var(--text-muted);
  }

  .side-venture {
    margin-top: 44px;
    text-align: left;
  }

  .venture-name {
    margin: 0;
    font-size: 25px;
    color: var(--text-muted);
  }

  .venture-note {
    margin: 6px 0 0;
    font-size: 21px;
    color: var(--text-muted);
  }

  .contact-list {
    list-style: none;
    margin: 52px 0 0;
    padding: 0;
    display: flex;
    flex-direction: column;
    gap: 16px;
  }

  .contact-item {
    display: flex;
    align-items: center;
    gap: 14px;
    font-size: 18px;
    color: var(--text-light);
  }

  .contact-item.email {
    font-size: 15px;
  }

  .contact-icon {
    width: 32px;
    height: 32px;
    flex: none;
  }
</style>
</head>
<body>
<main class="canvas">
  <section class="business-card" aria-label="Business card for Reid Calder">
    <div class="card-texture" role="img" aria-label="Dark background with a faint crossing diagonal line pattern"></div>

    <div class="card-content">
      <h1 class="holder-name">Reid Calder</h1>
      <p class="holder-role">Event Manager &amp; MC</p>

      <div class="side-venture">
        <p class="venture-name">Tressel Magazine</p>
        <p class="venture-note">The other event I run</p>
      </div>

      <ul class="contact-list">
        <li class="contact-item phone">
          <svg class="contact-icon" viewBox="0 0 32 32" aria-hidden="true">
            <circle cx="16" cy="16" r="14.5" fill="none" stroke="#f4f4f4" stroke-width="1.6"/>
            <path d="M11.5 9.5c.8-.6 1.6-.4 2 .3l1.2 2.2c.3.6.2 1.2-.3 1.6l-.9.7c.6 1.6 1.9 3 3.5 3.8l.8-.9c.4-.5 1-.6 1.6-.3l2.2 1.2c.7.4.9 1.2.3 2l-.9 1.1c-.6.7-1.6 1-2.5.7-4-1.4-7-4.5-8.3-8.5-.3-.9 0-1.9.7-2.5z" fill="none" stroke="#f4f4f4" stroke-width="1.5" stroke-linejoin="round"/>
          </svg>
          <span>820.555.0147</span>
        </li>
        <li class="contact-item email">
          <svg class="contact-icon" viewBox="0 0 32 32" aria-hidden="true">
            <circle cx="16" cy="16" r="14.5" fill="none" stroke="#f4f4f4" stroke-width="1.6"/>
            <rect x="9" y="11" width="14" height="10" fill="none" stroke="#f4f4f4" stroke-width="1.5" stroke-linejoin="round"/>
            <path d="M9 11l7 6 7-6" fill="none" stroke="#f4f4f4" stroke-width="1.5" stroke-linejoin="round"/>
          </svg>
          <span>ReidCalder@Tresselmag.com</span>
        </li>
      </ul>
    </div>
  </section>
</main>
</body>
</html>
```